Bref créative
Stationery for interior design business
Venmark Interiors, LLC
Simple
Cleo Venmark
Interior Designer
No address on card or stationery
cleo@venmarkinteriors.example
venmarkinteriors.example
Please also include my blog address on the front of the card: cleovenmark.example
Open for design suggestions, but I'd like either the entire logo or only the sphere to appear on the back

```html
<!DOCTYPE html>
<html lang="en">
<head>
<meta charset="utf-8">
<title>Venmark Interiors – Business Card</title>
<link rel="stylesheet" href="https://fonts.googleapis.com/css2?family=Open+Sans:wght@400;600&display=swap">
<style>
  :root {
    --page-bg: #e9e9ec;
    --card-white: #ffffff;
    --brand-blue: #3b47a1;
    --brand-blue-deep: #2f3a8c;
    --silver: #c9cbd3;
    --silver-dark: #9a9ca6;
    --ink-white: #ffffff;
    --icon-ink: #3b47a1;
    --logo-grey: #4a4a4f;
  }
  * { box-sizing: border-box; }
  html, body {
    margin: 0;
    width: 1200px;
    height: 900px;
    overflow: hidden;
    background: var(--page-bg);
    font-family: "Open Sans", Arial, sans-serif;
  }
  .canvas {
    position: relative;
    width: 1200px;
    height: 900px;
  }
  .business-card {
    position: absolute;
    left: 100px;
    top: 164px;
    width: 1000px;
    height: 572px;
    background: var(--card-white);
    box-shadow: 0 10px 30px rgba(0,0,0,0.18);
    overflow: hidden;
  }
  .brand-lockup {
    position: absolute;
    left: 48px;
    top: 60px;
    display: flex;
    align-items: center;
    gap: 22px;
  }
  .brand-dot {
    width: 120px;
    height: 120px;
    border-radius: 50%;
    background: var(--brand-blue);
  }
  .brand-name {
    font-size: 46px;
    font-weight: 400;
    color: var(--brand-blue);
    letter-spacing: 1px;
    line-height: 1;
  }
  .silver-rule {
    position: absolute;
    left: 0;
    right: 0;
    top: 236px;
    height: 12px;
    background: linear-gradient(to bottom, var(--silver), #eef0f4 50%, var(--silver-dark));
  }
  .contact-band {
    position: absolute;
    left: 0;
    right: 0;
    top: 248px;
    height: 244px;
    background: linear-gradient(to bottom, var(--brand-blue), var(--brand-blue-deep));
  }
  .band-foot-rule {
    position: absolute;
    left: 0;
    right: 0;
    top: 492px;
    height: 5px;
    background: var(--silver);
  }
  .designer {
    position: absolute;
    right: 52px;
    top: 40px;
    text-align: right;
    color: var(--ink-white);
  }
  .designer-name {
    margin: 0;
    font-size: 25px;
    font-weight: 600;
  }
  .designer-role {
    margin: 4px 0 0;
    font-size: 21px;
    font-weight: 400;
  }
  .contact-list {
    position: absolute;
    left: 46px;
    top: 60px;
    margin: 0;
    padding: 0;
    list-style: none;
    color: var(--ink-white);
    font-size: 21px;
  }
  .contact-item {
    display: flex;
    align-items: center;
    gap: 14px;
    height: 42px;
  }
  .contact-icon {
    width: 24px;
    height: 24px;
    flex: none;
  }
</style>
</head>
<body>
<main class="canvas">
  <section class="business-card" aria-label="Venmark Interiors business card">
    <div class="brand-lockup">
      <div class="brand-dot" aria-hidden="true"></div>
      <div class="brand-name">Venmark Interiors</div>
    </div>

    <div class="silver-rule"></div>
    <div class="contact-band">
      <div class="designer">
        <p class="designer-name">Cleo Venmark</p>
        <p class="designer-role">Interior Designer</p>
      </div>
      <ul class="contact-list">
        <li class="contact-item">
          <svg class="contact-icon" viewBox="0 0 24 24" aria-hidden="true">
            <circle cx="12" cy="12" r="12" fill="#fff"/>
            <path d="M8.2 6.5l2 2.2-1.1 1.5c.8 1.7 2 2.9 3.7 3.7l1.5-1.1 2.2 2-1 1.9c-4.3-.4-8.3-4.4-8.7-8.7z" fill="var(--icon-ink)"/>
          </svg>
          <span>555-014-2870</span>
        </li>
        <li class="contact-item">
          <svg class="contact-icon" viewBox="0 0 24 24" aria-hidden="true">
            <circle cx="12" cy="12" r="12" fill="#fff"/>
            <rect x="6" y="8" width="12" height="8.5" rx="1" fill="var(--icon-ink)"/>
            <path d="M6.5 8.6l5.5 4.2 5.5-4.2" stroke="#fff" stroke-width="1.2" fill="none"/>
          </svg>
          <span>cleo@venmarkinteriors.example</span>
        </li>
        <li class="contact-item">
          <svg class="contact-icon" viewBox="0 0 24 24" aria-hidden="true">
            <circle cx="12" cy="12" r="12" fill="#fff"/>
            <g stroke="var(--icon-ink)" stroke-width="1.3" fill="none">
              <circle cx="12" cy="12" r="6"/>
              <ellipse cx="12" cy="12" rx="2.6" ry="6"/>
              <path d="M6 12h12"/>
            </g>
          </svg>
          <span>www.venmarkinteriors.example</span>
        </li>
        <li class="contact-item">
          <svg class="contact-icon" viewBox="0 0 24 24" aria-hidden="true">
            <circle cx="12" cy="12" r="12" fill="#fff"/>
            <g stroke="var(--icon-ink)" stroke-width="1.3" fill="none">
              <circle cx="12" cy="12" r="6"/>
              <ellipse cx="12" cy="12" rx="2.6" ry="6"/>
              <path d="M6 12h12"/>
            </g>
          </svg>
          <span>www.cleovenmark.example</span>
        </li>
      </ul>
    </div>
    <div class="band-foot-rule"></div>
  </section>
</main>
</body>
</html>
```